Corporate Design für ein Installationsunternehmen
Wir sind mit dem Endergebnis sehr glücklich und zufrieden! Pelle ist auf alle unsere Wünsche und Vorschläge ohne zu zögern und mit viel Geduld eingegangen und wir können seine Arbeit wärmstens empfehlen. Vielen Dank nochmal Pelle für das tolle Design.
Zielgruppe
Wir sind ein Installationsunternehmen im Bereich Gas-, Wasser- und Heizung.
Aufgabenstellung
Das Symbol des Triskele sollte im Logo kreativ integriert werden ( wir sind jedoch offen auch für andere kreative Vorschläge die uns inspirieren).
Sauber, akkurat, symmetrisch und professionell soll es rüber kommen.
Das Symbol soll Vertrauen im Kunden wecken.

```html
<!DOCTYPE html>
<html lang="de">
<head>
<meta charset="utf-8">
<title>Velantra – Visitenkarte</title>
<link rel="stylesheet" href="https://fonts.googleapis.com/css2?family=Michroma&family=Quicksand:wght@500;600&display=swap">
<style>
  :root{
    --bg:#4a4d4f;
    --bg-light:#5d6163;
    --paper:#f4f4f2;
    --ink:#15161a;
    --navy:#0c1020;
    --navy-deep:#050710;
    --red:#d11f1f;
    --gold:#e0a81e;
    --blue:#1e88e5;
    --muted:#2b2d33;
    --light-text:#e8eaf0;
  }
  *{margin:0;padding:0;box-sizing:border-box}
  html,body{width:1200px;height:834px;overflow:hidden}
  body{
    background:radial-gradient(ellipse at 70% 30%,var(--bg-light),var(--bg) 70%);
    font-family:"Quicksand",sans-serif;
    position:relative;
  }
  .card{
    position:absolute;
    width:480px;height:274px;
    box-shadow:0 14px 30px rgba(0,0,0,.35);
  }
  .card--front{left:90px;top:280px;background:var(--paper);color:var(--ink)}
  .card--back{left:630px;top:280px;background:radial-gradient(ellipse at 50% 40%,var(--navy),var(--navy-deep) 80%)}

  .brand{position:absolute;left:40px;top:118px;display:flex;flex-direction:column;align-items:flex-start}
  .brand__row{display:flex;align-items:center;gap:10px}
  .brand__dot{width:14px;height:14px;border-radius:50%;background:var(--red)}
  .brand__name{font-family:"Quicksand",sans-serif;font-weight:600;font-size:30px;letter-spacing:2px;color:var(--ink)}
  .brand__tagline{margin-top:4px;margin-left:24px;font-size:9px;letter-spacing:2px;color:var(--muted)}

  .person{position:absolute;right:38px;top:34px;text-align:right}
  .person__name{font-family:"Michroma",sans-serif;font-size:20px;letter-spacing:1px}
  .person__role{font-family:"Michroma",sans-serif;font-size:11px;letter-spacing:1px;margin-top:4px}

  .contacts{position:absolute;right:38px;top:108px;list-style:none}
  .contacts li{display:flex;justify-content:flex-end;align-items:flex-start;gap:12px;font-size:10px;line-height:1.45;text-align:right;margin-bottom:12px}
  .contacts svg{width:12px;height:12px;flex:none;margin-top:1px}

  .card__rule{position:absolute;left:0;right:0;bottom:18px;height:3px;background:var(--ink)}

  .back__brand{position:absolute;left:0;right:0;top:98px;display:flex;justify-content:center;align-items:center;gap:12px}
  .back__dot{width:16px;height:16px;border-radius:50%;background:var(--red)}
  .back__name{font-family:"Quicksand",sans-serif;font-weight:600;font-size:34px;letter-spacing:3px;color:var(--light-text)}
  .back__url{position:absolute;left:0;right:0;bottom:52px;text-align:center;font-size:12px;letter-spacing:3px;color:var(--light-text)}
</style>
</head>
<body>
  <section class="card card--front">
    <div class="brand">
      <div class="brand__row">
        <span class="brand__dot"></span>
        <span class="brand__name">VELANTRA</span>
      </div>
      <span class="brand__tagline">GAS | WASSER | HEIZUNG</span>
    </div>

    <div class="person">
      <div class="person__name">LENN HARBO</div>
      <div class="person__role">CO - FOUNDER</div>
    </div>

    <ul class="contacts">
      <li><span>+44 1860 512 908</span>
        <svg viewBox="0 0 24 24" aria-hidden="true"><path fill="var(--red)" d="M6.6 10.8a15 15 0 0 0 6.6 6.6l2.2-2.2c.3-.3.7-.4 1-.2 1.1.4 2.3.6 3.6.6.6 0 1 .4 1 1V20c0 .6-.4 1-1 1A17 17 0 0 1 3 4c0-.6.4-1 1-1h3.5c.6 0 1 .4 1 1 0 1.3.2 2.5.6 3.6.1.3 0 .7-.2 1z"/></svg>
      </li>
      <li><span>lennharbo@velantra.com</span>
        <svg viewBox="0 0 24 24" aria-hidden="true"><rect x="2" y="5" width="20" height="14" rx="1" fill="var(--gold)"/><path d="M2 6l10 7 10-7" fill="none" stroke="#fff" stroke-width="1.5"/></svg>
      </li>
      <li><span>Velantra Technik Ltd<br>12 Norden Square, Ostwall<br>Hamburg</span>
        <svg viewBox="0 0 24 24" aria-hidden="true"><path fill="var(--blue)" d="M12 2a7 7 0 0 0-7 7c0 5 7 13 7 13s7-8 7-13a7 7 0 0 0-7-7zm0 9.5a2.5 2.5 0 1 1 0-5 2.5 2.5 0 0 1 0 5z"/></svg>
      </li>
    </ul>

    <div class="card__rule"></div>
  </section>

  <section class="card card--back">
    <div class="back__brand">
      <span class="back__dot"></span>
      <span class="back__name">VELANTRA</span>
    </div>
    <div class="back__url">WWW.VELANTRA.COM</div>
  </section>
</body>
</html>
```